Vegan Alfredo Sauce Label Design for Brambleway Pantry Co

We are a food co. committed to making vegan food more accessible to people who want to eat healthier. Our first line of product is vegan Alfredo sauce.
We have 3 flavors:
- Garlic
- Pesto
- Lemony Artichoke
The current project is the design for the first flavor: garlic. However, we would like a template that would translate well to other flavors, so they look like a family of products.
These will be in standard 16 oz jars. The whole label will be approx 6cm x 24cm, but the front visual space is approx 6cm x 10cm. The rest will be nutritional labeling and copy about the company.
We also need a stamp or font- based logo that says Brambleway Pantry Co. (or lower case: brambleway pantry co.), the name of the company.
The picture (attached) of Plantbased Nacho Dip is the closest to what we are going for. Because the sauce is creamy white, a colorful background with off-white font will be best.
We currently have a website, although we are doing a brand over-haul (hence, this posting) www.bramblewaypantryco.example. If the designer is a good fit, we have several more projects, in line.
Other brands we love: Tidewell Grocers, Marlow Ridge Provisions, Pulp Poured Daily.
The final brand should communicate hip, natural and health.
And personally, I love design that is clever and somehow makes me smile.
Target Market(s)
Vegans, vegetarians, and people with common food allergies - all ages.
Young, hip families.
Industry/Entity Type
It Company
Requirements
Must have
- Copy:
Vegan Alfredo or Vegan Alfredo Sauce
Garlic
Brambleway Pantry or Brambleway Pantry Co
16 oz
Nice to have
- May include copy:
Gluten-Free Soy-Free Nut-Free
Should not have
- Neon colors

```html
<!DOCTYPE html>
<html lang="en">
<head>
<meta charset="utf-8">
<title>Brambleway Pantry Co. – Vegan Alfredo Sauce Labels</title>
<link rel="stylesheet" href="https://fonts.googleapis.com/css2?family=Cinzel:wght@400&family=Lato:wght@300;400;700&display=swap">
<style>
  :root {
    --page: #ffffff;
    --ink: #1e1e1e;
    --cream: #fbf1d6;
    --subtitle: #4a4a4a;
    --garlic-a: #c88887;
    --garlic-b: #d49f9d;
    --garlic-art: #b98770;
    --artichoke-a: #d8bb14;
    --artichoke-b: #e3c93e;
    --artichoke-art: #7f9a45;
    --pesto-a: #7c9a26;
    --pesto-b: #95ae45;
    --pesto-art: #3f6b2a;
  }
  * { box-sizing: border-box; margin: 0; padding: 0; }
  html, body {
    width: 1200px; height: 900px; overflow: hidden;
    background: var(--page);
  }
  .canvas { position: relative; width: 1200px; height: 900px; }
  .option-title {
    position: absolute; left: 34px; top: 28px;
    font-family: "Cinzel", serif; font-size: 22px; letter-spacing: 5px;
    color: var(--ink);
  }
  .label-row {
    position: absolute; left: 0; top: 300px; width: 1200px;
    display: flex; justify-content: center; gap: 36px;
  }
  .label {
    position: relative; width: 245px; height: 245px;
    display: flex; flex-direction: column; align-items: center;
    color: var(--cream); text-align: center;
    background: repeating-linear-gradient(90deg, var(--a) 0 14px, var(--b) 14px 28px);
  }
  .label--garlic { --a: var(--garlic-a); --b: var(--garlic-b); --art: var(--garlic-art); }
  .label--artichoke { --a: var(--artichoke-a); --b: var(--artichoke-b); --art: var(--artichoke-art); }
  .label--pesto { --a: var(--pesto-a); --b: var(--pesto-b); --art: var(--pesto-art); }

  .brand {
    margin-top: 24px; display: flex; align-items: center; gap: 5px;
    font-family: "Lato", sans-serif; font-weight: 400; font-size: 13px;
    color: var(--cream); letter-spacing: 0.2px;
  }
  .brand-dot { width: 8px; height: 8px; border-radius: 50%; background: var(--cream); }
  .flavor-art {
    margin-top: 12px; width: 76px; height: 76px; border-radius: 50%;
    background: radial-gradient(circle, var(--art) 30%, transparent 72%);
  }
  .flavor-prefix {
    margin-top: 0; font-family: "Cinzel", serif; font-size: 13px;
    letter-spacing: 3px; line-height: 14px;
  }
  .flavor-name {
    font-family: "Cinzel", serif; font-size: 36px; letter-spacing: 2.5px;
    line-height: 38px; margin-top: 8px;
  }
  .flavor-prefix + .flavor-name { margin-top: 0; font-size: 32px; }
  .product-type {
    font-family: "Lato", sans-serif; font-weight: 700; font-size: 10.5px;
    letter-spacing: 1.2px; color: var(--subtitle); margin-top: 4px;
  }
  .claims {
    margin-top: 14px; display: flex; align-items: baseline; gap: 6px;
    font-family: "Lato", sans-serif; font-weight: 400; font-size: 10px;
    letter-spacing: 0.6px; white-space: nowrap;
  }
  .claims .net { font-size: 14px; letter-spacing: 0; margin-left: 2px; }
</style>
</head>
<body>
<main class="canvas">
  <h1 class="option-title">OPTION 1</h1>

  <section class="label-row">
    <article class="label label--garlic">
      <div class="brand"><span class="brand-dot"></span>brambleway pantry co</div>
      <div class="flavor-art" role="img" aria-label="Illustration of garlic cloves arranged like a flower around a garlic bulb"></div>
      <h2 class="flavor-name">GARLIC</h2>
      <p class="product-type">VEGAN ALFREDO SAUCE</p>
      <p class="claims">GLUTEN-FREE • SOY-FREE • NUT-FREE <span class="net">16oz</span></p>
    </article>

    <article class="label label--artichoke">
      <div class="brand"><span class="brand-dot"></span>brambleway pantry co</div>
      <div class="flavor-art" role="img" aria-label="Illustration of four artichokes around a lemon slice"></div>
      <p class="flavor-prefix">LEMONY</p>
      <h2 class="flavor-name">ARTICHOKE</h2>
      <p class="product-type">VEGAN ALFREDO SAUCE</p>
      <p class="claims">GLUTEN-FREE • SOY-FREE • NUT-FREE <span class="net">16oz</span></p>
    </article>

    <article class="label label--pesto">
      <div class="brand"><span class="brand-dot"></span>brambleway pantry co</div>
      <div class="flavor-art" role="img" aria-label="Illustration of basil leaves with a garlic bulb"></div>
      <h2 class="flavor-name">PESTO</h2>
      <p class="product-type">VEGAN ALFREDO SAUCE</p>
      <p class="claims">GLUTEN-FREE • SOY-FREE • NUT-FREE <span class="net">16oz</span></p>
    </article>
  </section>
</main>
</body>
</html>
```